Harborline Crest Insurance Services

we are a high end insurance agency we specialize on Auto | Home | Business | Life looking for something professional and luxuries at the same time. if you guys need anything else please let me know.

Auto | Home | Business | Life must be under logo on the back with black background.

i want the back part to be black with our gold logo on it.

Target Market(s)

Auto | Home | Business | Life

Industry/Entity Type

Insurance Broker

Contact Information for Business Card

My logo is gold so a black in the back would be nice.

Font styles to use
Serif

Colors
000000

Requirements
Must have
• Big logo on the back with black background.

```html
<!DOCTYPE html>
<html lang="en">
<head>
<meta charset="utf-8">
<title>Harborline Crest Insurance Services – Business Card</title>
<link href="https://fonts.googleapis.com/css2?family=Tinos:wght@400;700&display=swap" rel="stylesheet">
<style>
  :root {
    --stage: #232323;
    --card: #0d0d0d;
    --facet-light: #2a2a2a;
    --facet-dark: #070707;
    --gold: #f2c12e;
    --silver: #b9b9b9;
    --white: #f1f1f1;
  }
  * { margin: 0; padding: 0; box-sizing: border-box; }
  html, body {
    width: 1200px; height: 1189px; overflow: hidden;
    background: var(--stage);
    font-family: "Tinos", "Times New Roman", serif;
  }
  .sheet {
    position: relative; width: 1200px; height: 1189px;
    display: flex; flex-direction: column; align-items: center;
    justify-content: center; gap: 56px;
  }
  .card {
    position: relative; width: 900px; height: 514px;
    border-radius: 30px; overflow: hidden;
    background: var(--card);
    box-shadow: 0 18px 40px rgba(0,0,0,.55);
  }
  .card__texture {
    position: absolute; inset: 0;
    background:
      linear-gradient(130deg, var(--facet-light) 0%, transparent 35%),
      linear-gradient(300deg, var(--facet-light) 0%, transparent 40%),
      linear-gradient(200deg, var(--facet-dark) 20%, #1b1b1b 55%, var(--facet-dark) 90%);
  }
  /* Back: large brand mark */
  .brand-big {
    position: absolute; inset: 0;
    display: flex; flex-direction: column; align-items: center; justify-content: center; gap: 20px;
  }
  .brand-big__dot {
    width: 110px; height: 110px; border-radius: 50%; background: var(--gold);
  }
  .brand-big__name {
    color: var(--gold); font-weight: 700; font-size: 42px;
    letter-spacing: 3px; text-transform: uppercase; text-align: center; line-height: 1.2;
  }
  .brand-big__lines {
    color: var(--silver); font-size: 20px; letter-spacing: 5px;
    text-transform: uppercase; text-align: center;
  }
  /* Front */
  .brand-small {
    position: absolute; left: 60px; top: 60px;
    display: flex; align-items: center; gap: 22px;
  }
  .brand-small__dot { width: 76px; height: 76px; border-radius: 50%; background: var(--gold); }
  .brand-small__name {
    color: var(--gold); font-weight: 700; font-size: 30px;
    letter-spacing: 2px; text-transform: uppercase; line-height: 1.2;
  }
  .person {
    position: absolute; right: 60px; top: 196px;
    display: flex; flex-direction: column; align-items: flex-end;
  }
  .person__name {
    color: var(--gold); font-weight: 700; font-size: 26px; letter-spacing: 1px;
  }
  .person__role { color: var(--white); font-size: 22px; margin-top: 4px; }
  .rule {
    position: absolute; left: 60px; right: 60px; top: 300px;
    height: 2px; background: var(--gold);
  }
  .contacts {
    position: absolute; left: 60px; bottom: 50px; list-style: none;
  }
  .contacts li {
    display: flex; align-items: center; gap: 14px;
    color: var(--white); font-size: 24px; line-height: 36px;
  }
  .contacts svg { width: 22px; height: 22px; flex: none; }
  .address {
    position: absolute; right: 60px; bottom: 62px; text-align: right;
    color: var(--white); font-size: 22px; line-height: 30px;
  }
</style>
</head>
<body>
<main class="sheet">

  <section class="card card--back">
    <div class="card__texture" role="img" aria-label="Dark faceted crystal pattern background"></div>
    <div class="brand-big">
      <span class="brand-big__dot"></span>
      <p class="brand-big__name">Harborline Crest<br>Insurance Services</p>
      <p class="brand-big__lines">Auto | Home | Business | Life</p>
    </div>
  </section>

  <section class="card card--front">
    <div class="card__texture" role="img" aria-label="Dark faceted crystal pattern background"></div>

    <div class="brand-small">
      <span class="brand-small__dot"></span>
      <p class="brand-small__name">Harborline Crest<br>Insurance Services</p>
    </div>

    <div class="person">
      <p class="person__name">NOLAN REYES</p>
      <p class="person__role">Director</p>
    </div>

    <div class="rule"></div>

    <ul class="contacts">
      <li>
        <svg viewBox="0 0 24 24" aria-hidden="true"><path fill="#f2c12e" d="M6.6 10.8a15.2 15.2 0 0 0 6.6 6.6l2.2-2.2c.3-.3.7-.4 1-.2 1.1.4 2.3.6 3.6.6.6 0 1 .4 1 1V20c0 .6-.4 1-1 1A17 17 0 0 1 3 4c0-.6.4-1 1-1h3.5c.6 0 1 .4 1 1 0 1.3.2 2.5.6 3.6.1.3 0 .7-.2 1z"/></svg>
        555 014 2290
      </li>
      <li>
        <svg viewBox="0 0 24 24" aria-hidden="true"><rect x="2" y="5" width="20" height="14" rx="1" fill="#f2c12e"/><path d="M2 6l10 7 10-7" fill="none" stroke="#0d0d0d" stroke-width="1.6"/></svg>
        info@harborlinecrest.com
      </li>
      <li>
        <svg viewBox="0 0 24 24" aria-hidden="true"><g fill="none" stroke="#f2c12e" stroke-width="1.8"><circle cx="12" cy="12" r="9.5"/><ellipse cx="12" cy="12" rx="4" ry="9.5"/><path d="M2.5 12h19M4 7h16M4 17h16"/></g></svg>
        www.harborlinecrest.com
      </li>
    </ul>

    <p class="address">PO BOX 418 Quayside Road,<br>7th Avenue Portmere, USA</p>
  </section>

</main>
</body>
</html>
```